Business card for builder specialising in renovations.

Need a card for our building business. Business name is under Martin Pelloe.
Have licence number on card ( 527916K)
Contact number (0400 382 615)
Want to work on logo for some business cards and shirts - something with MP or MPB or open to ideas??
No animations, No hammers. Something sharp and eye catching.
Highlight that we are a renovation specialist. Simple on front with extra details on back with some lines to jot down things.

Target Market(s)

Renovators

Industry/Entity Type

Building

Contact Information for Business Card

2 sided with room on back to jot things down.
Extra details on back so front can be simple ..like, renovations, bathrooms, decks, extensions, new builds,

Logo Text

MP

Font styles to use
Serif

Requirements
Must have
• Eye catching design .
• Name : Martin pelloe
• Licence number
• Contact number - 0400382615
Nice to have
• Some logo design that we can carry through to other forms of advertising
• Local builder
• Quality work
Should not have
• No animations

```html
<!DOCTYPE html>
<html lang="en">
<head>
<meta charset="utf-8">
<title>Martin Pelloe – Business Card</title>
<link href="https://fonts.googleapis.com/css2?family=PT+Sans:wght@400;700&display=swap" rel="stylesheet">
<style>
  :root {
    --backdrop: #3b3531;
    --card-black: #050505;
    --card-sheen: #1c1c1c;
    --brand-blue: #0aa3d8;
    --stripe-grey: #d9d9d9;
    --text-white: #ffffff;
  }
  * { margin: 0; padding: 0; box-sizing: border-box; }
  html, body {
    width: 1200px;
    height: 844px;
    overflow: hidden;
    background: var(--backdrop);
    font-family: "PT Sans", "Helvetica Neue", Arial, sans-serif;
  }
  .stage {
    position: relative;
    width: 1200px;
    height: 844px;
  }
  .card {
    position: absolute;
    top: 272px;
    width: 520px;
    height: 300px;
    overflow: hidden;
    box-shadow: 0 12px 30px rgba(0,0,0,0.45);
  }

  /* Back side: contact details */
  .card-back {
    left: 50px;
    background: linear-gradient(110deg, var(--card-black) 60%, var(--card-sheen) 100%);
  }
  .card-back .band {
    position: absolute;
    left: 0;
    width: 100%;
    height: 13px;
    background: var(--brand-blue);
  }
  .card-back .band-top { top: 0; }
  .card-back .band-bottom { bottom: 0; }
  .contact {
    position: absolute;
    top: 96px;
    left: 0;
    width: 100%;
    text-align: center;
    color: var(--text-white);
  }
  .contact-name {
    color: var(--brand-blue);
    font-weight: 700;
    font-size: 25px;
    margin-bottom: 24px;
  }
  .contact-phone {
    font-size: 17px;
    margin-bottom: 8px;
  }
  .contact-licence {
    font-size: 17px;
    font-weight: 700;
  }

  /* Front side: brand */
  .card-front {
    left: 630px;
    background: radial-gradient(ellipse at 55% 35%, var(--card-sheen) 0%, var(--card-black) 65%);
  }
  .edge-tab {
    position: absolute;
    width: 24px;
    height: 44px;
    background: var(--brand-blue);
  }
  .edge-tab::after {
    content: "";
    position: absolute;
    top: 0;
    width: 4px;
    height: 100%;
    background: var(--stripe-grey);
  }
  .edge-tab-left { left: 0; top: 168px; }
  .edge-tab-left::after { right: 0; }
  .edge-tab-right { right: 0; top: 48px; }
  .edge-tab-right::after { left: 0; }

  .brand {
    position: absolute;
    top: 92px;
    left: 0;
    width: 100%;
    display: flex;
    justify-content: center;
    align-items: center;
    gap: 14px;
  }
  .brand-square {
    width: 30px;
    height: 30px;
    background: var(--brand-blue);
  }
  .brand-name {
    color: var(--brand-blue);
    font-weight: 700;
    font-size: 36px;
    line-height: 1;
  }
  .services {
    position: absolute;
    top: 170px;
    left: 0;
    width: 100%;
    text-align: center;
    color: var(--brand-blue);
    font-weight: 700;
    font-size: 16px;
    line-height: 1.3;
  }
</style>
</head>
<body>
  <main class="stage">
    <section class="card card-back" aria-label="Business card, back">
      <div class="band band-top"></div>
      <div class="contact">
        <p class="contact-name">Martin Pelloe</p>
        <p class="contact-phone">0400 382 615</p>
        <p class="contact-licence">License No- 527916K</p>
      </div>
      <div class="band band-bottom"></div>
    </section>

    <section class="card card-front" aria-label="Business card, front">
      <div class="edge-tab edge-tab-right"></div>
      <div class="brand">
        <span class="brand-square"></span>
        <span class="brand-name">Martin Pelloe</span>
      </div>
      <p class="services">Rrenovations, bathrooms, decks,<br>extensions, new builds etc</p>
      <div class="edge-tab edge-tab-left"></div>
    </section>
  </main>
</body>
</html>
```